Torvane Staffing - Mission Poster Design

We are a staffing and recruiting firm with multiple locations across the US. I am seeking a clean modern design highlighting our Mission Statement: Torvane Staffing...Linking Bright Talent with Bold Employers! This design will be framed and placed at the entrance of all of our offices. My website is www.torvanestaffing.example

Target Market(s)

Will be our company mission with a poster prominently placed in each office.

Industry/Entity Type

Staffing

Requirements
Must have
• Must be professional, clean and eye catching. We want to embrace diversity, so we like a variety of people if people will be a focal part.

```html
<!DOCTYPE html>
<html lang="en">
<head>
<meta charset="utf-8">
<title>Torvane Staffing – Mission Poster</title>
<link rel="stylesheet" href="https://fonts.googleapis.com/css2?family=Figtree:wght@400;700;800&display=swap">
<style>
  :root {
    --poster-yellow: #ecc233;
    --poster-yellow-deep: #e2b324;
    --ring-tint: rgba(255, 255, 255, 0.35);
    --brand-red: #e5413a;
    --brand-green: #247a45;
    --brand-gold: #d9bb2a;
    --brand-navy: #343167;
    --rule-grey: #8a8a8a;
    --paper: #ffffff;
  }
  * { margin: 0; padding: 0; box-sizing: border-box; }
  html, body {
    width: 910px;
    height: 1200px;
    overflow: hidden;
    background: var(--paper);
  }
  .poster {
    position: relative;
    width: 910px;
    height: 1200px;
    overflow: hidden;
    background: var(--paper);
    font-family: "Figtree", "Helvetica Neue", Arial, sans-serif;
  }
  .poster__backdrop {
    position: absolute;
    inset: 0;
    width: 910px;
    height: 1200px;
  }
  .brand {
    position: absolute;
    left: 0;
    width: 910px;
    top: 168px;
    text-align: center;
    color: var(--brand-navy);
    font-weight: 800;
    line-height: 1;
  }
  .brand__name {
    display: block;
    font-size: 104px;
    letter-spacing: -1px;
  }
  .brand__sub {
    display: block;
    font-size: 34px;
    margin-top: 10px;
    padding-left: 230px;
    letter-spacing: 1px;
  }
  .mission {
    position: absolute;
    left: 0;
    width: 910px;
    top: 380px;
    text-align: center;
    font-weight: 800;
    text-transform: uppercase;
    font-size: 60px;
    line-height: 64px;
    letter-spacing: -0.5px;
  }
  .mission__line { display: block; }
  .mission__line--red { color: var(--brand-red); }
  .mission__line--green { color: var(--brand-green); }
  .mission__line--gold { color: var(--brand-gold); }
  .mission__line--navy { color: var(--brand-navy); }
  .team-photo {
    position: absolute;
    left: 68px;
    top: 662px;
    width: 790px;
    height: 538px;
    border-radius: 260px 260px 0 0;
    background:
      linear-gradient(180deg, rgba(201, 150, 120, 0.0) 0%, rgba(60, 80, 120, 0.55) 100%),
      linear-gradient(90deg, #9e9a92 0%, #e9e6e2 18%, #e2a62a 32%, #d98a8f 50%, #ef7a5d 62%, #e8cf49 74%, #8fc6c8 86%, #3c6b3a 100%);
  }
  .website {
    position: absolute;
    left: 0;
    width: 910px;
    top: 1112px;
    text-align: center;
    color: var(--paper);
    font-weight: 700;
    font-size: 30px;
    letter-spacing: 0.2px;
  }
</style>
</head>
<body>
  <main class="poster">
    <svg class="poster__backdrop" viewBox="0 0 910 1200" aria-hidden="false">
      <defs>
        <linearGradient id="office-tone" x1="0" y1="0" x2="0" y2="1">
          <stop offset="0" stop-color="var(--poster-yellow)"/>
          <stop offset="1" stop-color="var(--poster-yellow-deep)"/>
        </linearGradient>
      </defs>
      <g role="img" aria-label="Office interior photograph toned in yellow">
        <rect class="backdrop__top" x="0" y="0" width="910" height="380" fill="url(#office-tone)"/>
        <circle class="backdrop__bowl" cx="455" cy="375" r="588" fill="url(#office-tone)" stroke="var(--brand-navy)" stroke-width="7"/>
      </g>
      <circle class="halo-ring" cx="455" cy="440" r="390" fill="var(--ring-tint)"/>
      <circle class="halo-disc" cx="455" cy="440" r="370" fill="var(--paper)"/>
      <g class="crop-marks" stroke="var(--rule-grey)" stroke-width="1" fill="none">
        <line x1="211" y1="358" x2="345" y2="358"/>
        <line x1="232" y1="342" x2="232" y2="420"/>
        <line x1="625" y1="641" x2="758" y2="641"/>
        <line x1="737" y1="582" x2="737" y2="658"/>
      </g>
    </svg>

    <div class="brand">
      <span class="brand__name">Torvane</span>
      <span class="brand__sub">staffing</span>
    </div>

    <h1 class="mission">
      <span class="mission__line mission__line--red">Linking</span>
      <span class="mission__line mission__line--green">Bright Talent</span>
      <span class="mission__line mission__line--gold">With Bold</span>
      <span class="mission__line mission__line--navy">Employers!</span>
    </h1>

    <div class="team-photo" role="img" aria-label="Photograph of a diverse group of smiling colleagues standing together in casual colourful clothing"></div>

    <p class="website">www.torvanestaffing.example</p>
  </main>
</body>
</html>
```